Typing Service Business Card Design

Need a new business card design for new logo update. The Keyline Crew is an outsourced typing service. We type audio / voice files into word documents. We are a professional service that is recognised in the industry over the past 15 years and have a strong connection to our brand. The final design should be professional, simple, yet effective.

Business

Contact Information for Business Card

Rosalind Varga
Director

rosalind@kbq.com.au
www.thekeylinecrewbase.com.au

```html
<!DOCTYPE html>
<html lang="en">
<head>
<meta charset="utf-8">
<title>The Keyline Crew – Business Card</title>
<link rel="stylesheet" href="https://fonts.googleapis.com/css2?family=Archivo+Black&family=Open+Sans:wght@400;600;700&display=swap">
<style>
  :root {
    --page: #ecebe8;
    --card: #ffffff;
    --ink: #1a1a1a;
    --grey: #555555;
    --magenta: #e0268f;
    --sky: #d9e8f5;
    --sign-blue: #3f86d6;
    --sign-blue-dark: #2a67b5;
    --wave-dark: #5a5a5a;
    --wave-light: #bdbdbd;
  }
  * { box-sizing: border-box; margin: 0; padding: 0; }
  html, body { width: 1200px; height: 900px; overflow: hidden; }
  body {
    background: var(--page);
    font-family: "Open Sans", Arial, sans-serif;
    display: flex;
    flex-direction: column;
    align-items: center;
    justify-content: center;
    gap: 36px;
  }
  .card {
    position: relative;
    width: 700px;
    height: 400px;
    background: var(--card);
    box-shadow: 0 6px 22px rgba(0,0,0,.18);
    overflow: hidden;
  }

  /* contact side */
  .keyboard-photo {
    position: absolute;
    right: 0; top: 0;
    width: 470px; height: 300px;
    background: linear-gradient(200deg, #c9ccd0 0%, #e6e7e9 40%, rgba(255,255,255,0) 80%);
  }
  .person-name {
    position: absolute; left: 44px; top: 56px;
    color: var(--magenta); font-size: 24px; font-weight: 600;
  }
  .person-role {
    position: absolute; left: 44px; top: 88px;
    color: var(--grey); font-size: 17px;
  }
  .contact-list {
    position: absolute; left: 44px; bottom: 46px;
    list-style: none; font-size: 16px; color: var(--ink);
  }
  .contact-list li { display: flex; align-items: center; gap: 10px; line-height: 26px; }
  .contact-tag {
    width: 16px; height: 16px; border-radius: 3px;
    background: linear-gradient(#f2f2f2, #cfcfcf);
    font-size: 10px; color: var(--grey);
    display: inline-flex; align-items: center; justify-content: center;
  }

  /* brand side */
  .brand-side {
    background: linear-gradient(180deg, var(--sky) 0%, #f3f7fb 45%, #ffffff 70%);
  }
  .solutions-photo {
    position: absolute; right: 0; top: 0;
    width: 330px; height: 190px;
    background: linear-gradient(160deg, #cfe0f1 0%, #eef3f8 60%, rgba(255,255,255,0) 100%);
  }
  .solutions-sign {
    position: absolute; left: 410px; top: 90px;
    width: 260px; height: 72px;
    background: linear-gradient(180deg, var(--sign-blue), var(--sign-blue-dark));
    color: #fff; font-family: "Archivo Black", Arial, sans-serif;
    font-size: 40px; display: flex; align-items: center; justify-content: center;
  }
  .tagline {
    position: absolute; left: 40px; top: 132px;
    font-family: "Archivo Black", Arial, sans-serif;
    font-size: 27px; color: var(--ink);
  }
  .waveform {
    position: absolute; left: 40px; top: 190px;
    width: 330px; height: 80px;
    background: linear-gradient(90deg, var(--wave-light) 0%, var(--wave-dark) 100%);
    opacity: .8;
  }
  .flow-icons { position: absolute; left: 395px; top: 182px; }
  .brand-name {
    position: absolute; right: 40px; top: 268px;
    color: var(--magenta); font-size: 34px; font-weight: 600;
    white-space: nowrap;
  }
</style>
</head>
<body>

  <section class="card contact-side">
    <div class="keyboard-photo" role="img" aria-label="Faded photo of hands typing on a keyboard"></div>
    <h1 class="person-name">Rosalind Varga</h1>
    <p class="person-role">Director</p>
    <ul class="contact-list">
      <li><span class="contact-tag">e</span>rosalind@kbq.com.au</li>
      <li><span class="contact-tag">w</span>www.thekeylinecrewbase.com.au</li>
    </ul>
  </section>

  <section class="card brand-side">
    <div class="solutions-photo" role="img" aria-label="Photo of a hand holding up a sign"></div>
    <div class="solutions-sign">Solutions</div>
    <p class="tagline">You talk. We type.</p>

    <div class="waveform" role="img" aria-label="Audio waveform illustration"></div>

    <svg class="flow-icons" width="150" height="50" viewBox="0 0 150 50" aria-hidden="true">
      <g fill="none" stroke="#333" stroke-width="2" stroke-linejoin="round">
        <path d="M12 8 Q4 8 4 16 V36 Q4 44 12 44"/>
        <path d="M12 20 H34 V12 L50 26 L34 40 V32 H12 Z"/>
        <path d="M76 8 H90 L96 14 V38 H76 Z"/>
        <path d="M80 18 H92 M80 24 H92 M80 30 H92"/>
        <path d="M104 8 H118 L124 14 V38 H104 Z"/>
        <path d="M108 18 H120 M108 24 H120 M108 30 H120"/>
      </g>
    </svg>

    <p class="brand-name">The Keyline Crew</p>
  </section>

</body>
</html>
```